Postcard Design

Law office.
Details are on the attached pdf file:
NOTE: the following items are to be changed, as follows:
1. price is 799
2. delete "Expires 2-8-13"
3. make "Nevada County's..." into "Northern California's ... "
4. Someplace where it fits nicely, add "Fast, Easy, Done!"
5. Delete "no obligation first visit"
6. That attached pdf was a successful ad so I want to maintain that look GENERALLY, but I'm not stuck on anything in particular. Some freedom to play with it for a perfect ad.
7. I'll attach the revised picture and the logo.

```html
<!DOCTYPE html>
<html lang="en">
<head>
<meta charset="utf-8">
<title>Moreno Law Postcard</title>
<link rel="stylesheet" href="https://fonts.googleapis.com/css2?family=Cormorant+Garamond:wght@400;500;600&family=Libre+Baskerville:ital,wght@0,700;1,700&family=Sorts+Mill+Goudy&family=Hind:wght@600&display=swap">
<style>
  :root {
    --ink: #141414;
    --panel: rgba(240, 238, 236, 0.8);
    --panel-edge: rgba(255, 255, 255, 0.55);
    --bg-dark: #1c1714;
    --bg-warm: #c89a58;
    --bg-mid: #6b5a4c;
    --suit: #1d1c1e;
    --skin: #c08a70;
    --name-box: rgba(255, 255, 255, 0.9);
    --muted: #333;
  }
  * { box-sizing: border-box; margin: 0; padding: 0; }
  html, body { width: 1200px; height: 880px; overflow: hidden; background: #fff; }

  .postcard {
    position: relative;
    width: 1200px;
    height: 880px;
    overflow: hidden;
    background:
      radial-gradient(ellipse 420px 260px at 160px 90px, var(--bg-warm), transparent 70%),
      linear-gradient(135deg, var(--bg-mid) 0%, var(--bg-dark) 45%, #3a302a 100%);
    color: var(--ink);
  }

  .office-backdrop {
    position: absolute; inset: 0;
    background: linear-gradient(90deg, rgba(90,70,55,0.25), rgba(230,220,210,0.2));
  }

  .attorney-portrait {
    position: absolute;
    left: 20px; top: 130px;
    width: 500px; height: 620px;
    border-radius: 250px 250px 0 0;
    background: linear-gradient(180deg, var(--skin) 0%, #9a6e58 32%, #3a3234 50%, var(--suit) 70%, #121113 100%);
    box-shadow: 0 0 40px rgba(0,0,0,0.35);
  }

  .brand-corner {
    position: absolute; left: 10px; top: 14px;
    display: flex; align-items: center; gap: 6px;
    font: 600 17px "Cormorant Garamond", serif;
    color: #2a2118;
  }
  .brand-corner .mark { width: 16px; height: 16px; border: 1.5px solid #2a2118; }

  .offer-panel {
    position: absolute;
    left: 496px; top: 18px;
    width: 692px; height: 844px;
    background: var(--panel);
    border: 1px solid var(--panel-edge);
    text-align: center;
  }

  .headline {
    margin-top: 14px;
    font: 600 52px/1.18 "Hind", sans-serif;
    letter-spacing: 0.5px;
  }
  .services {
    margin-top: 16px;
    font: 27px "Sorts Mill Goudy", serif;
  }
  .tagline {
    margin-top: 28px;
    font: 700 40px "Libre Baskerville", serif;
    letter-spacing: -0.5px;
  }
  .price {
    margin-top: 22px;
    font: italic 700 56px "Libre Baskerville", serif;
  }
  .value {
    margin-top: 6px;
    font: 24px "Sorts Mill Goudy", serif;
  }
  .slogan {
    margin-top: 30px;
    font: italic 700 56px "Libre Baskerville", serif;
    letter-spacing: -0.5px;
  }
  .call-prompt {
    margin-top: 40px;
    font: 600 36px "Cormorant Garamond", serif;
  }
  .phone {
    margin-top: 12px;
    display: inline-flex; align-items: center; gap: 18px;
    font: italic 700 52px "Libre Baskerville", serif;
    margin-left: 10px;
  }
  .phone svg { width: 32px; height: 32px; }

  .web-block {
    position: absolute; left: 69px; top: 704px;
    text-align: left;
  }
  .web-label { font: 600 26px "Cormorant Garamond", serif; }
  .web-url {
    margin-top: 10px; margin-left: 76px;
    display: flex; align-items: center; gap: 10px;
    font: 600 29px "Cormorant Garamond", serif;
    letter-spacing: 0.5px;
  }
  .web-url svg { width: 22px; height: 22px; }
  .extra {
    position: absolute; left: 238px; top: 810px;
    font: 18px "Sorts Mill Goudy", serif;
    color: var(--muted);
  }

  .firm-badge {
    position: absolute; left: 546px; top: 636px;
    width: 130px;
    display: flex; flex-direction: column; align-items: center;
  }
  .firm-badge .mark {
    width: 118px; height: 150px;
    border: 2px solid var(--ink); background: #fff;
    display: flex; align-items: center; justify-content: center;
    font: 600 22px/1.1 "Cormorant Garamond", serif;
  }
  .firm-badge .since {
    margin-top: 6px;
    font: 20px/1.3 "Cormorant Garamond", serif;
    white-space: nowrap;
    text-align: center;
  }

  .name-plate {
    position: absolute; left: 17px; top: 729px;
    width: 549px; height: 138px;
    background: var(--name-box);
    padding: 18px 0 0 10px;
    text-align: left;
  }
  .name-plate .prefix {
    margin-left: 110px;
    font: 400 29px/1 "Cormorant Garamond", serif;
  }
  .name-plate .attorney-name {
    margin-top: 8px;
    font: 500 72px/1 "Cormorant Garamond", serif;
    letter-spacing: -0.5px;
  }
</style>
</head>
<body>
<main class="postcard">
  <div class="office-backdrop" role="img" aria-label="Softly blurred law office interior in warm amber and cream tones"></div>
  <div class="attorney-portrait" role="img" aria-label="Portrait photo of the attorney in a dark suit and striped tie"></div>

  <div class="brand-corner"><span class="mark"></span>Moreno Law</div>

  <section class="offer-panel">
    <h1 class="headline">Northern California's<br>Best in Estate Plans</h1>
    <p class="services">Living Trusts, Wills &amp; All Necessary Documents</p>
    <p class="tagline">Protect Your Loved Ones!</p>
    <p class="price">$799</p>
    <p class="value">Over $2,000 value</p>
    <p class="slogan">Fast, Easy, Done!</p>
    <p class="call-prompt">It’s Easy - Call Now!</p>
    <p class="phone">
      <svg viewBox="0 0 24 24" aria-hidden="true"><path fill="#141414" d="M6.6 10.8a15.1 15.1 0 0 0 6.6 6.6l2.2-2.2c.3-.3.7-.4 1-.2 1.1.4 2.3.6 3.6.6.6 0 1 .4 1 1V20c0 .6-.4 1-1 1A17 17 0 0 1 3 4c0-.6.4-1 1-1h3.5c.6 0 1 .4 1 1 0 1.3.2 2.5.6 3.6.1.3 0 .7-.2 1z"/></svg>
      555-0142
    </p>

    <div class="web-block">
      <p class="web-label">Check me out at :</p>
      <p class="web-url">
        <svg viewBox="0 0 24 24" aria-hidden="true" fill="none" stroke="#141414" stroke-width="1.6"><circle cx="12" cy="12" r="10"/><ellipse cx="12" cy="12" rx="4.5" ry="10"/><path d="M2 12h20M4 6.5h16M4 17.5h16"/></svg>
        www.DanielMoreno.com
      </p>
    </div>
    <p class="extra">◆ Free Notarization</p>

    <div class="firm-badge">
      <div class="mark">Moreno<br>Law</div>
      <p class="since">Thousands Served<br>Since 1998</p>
    </div>
  </section>

  <div class="name-plate">
    <p class="prefix">Law Office Of</p>
    <p class="attorney-name">Daniel R. Moreno</p>
  </div>
</main>
</body>
</html>
```